KESTREL BOILWORKS business card

We need a new business card for our company "Kestrel Boilworks". The company is very simple, we supply bulk heated water to the oilfield and industry. I have included a few images of cards that I like so that you have an idea of the direction I want to go. I will leave fonts up to the designer. I have also included our logo.
Updates

Hello Designers,  if there are any more submissions coming in you might consider using other background colors than black.  I am looking for a little bit of variety before making the decision.

Thanks,

Dean

Sorry, I meant to say background colors other than just black and white.

Thanks,

Dean

Target Market(s)

Ages 20 to 60. Oilfield consultants and Oil and Gas Companies

Industry/Entity Type

Business

Font styles to use
Sans Serif

Requirements
Must have
• Dean Varga

email info@kestrelboilworks-mail.com

Phone # 780-555-3817
Fax 780-555-2964

Site 317, Box 4, Comp 2, RR5
Vellmoor Ridge, KR, T9K 4P3

11-07-52-3 W4M
Hwy 734 Between RR57 & RR58

**Must have our logo

Nice to have
• Would be nice to have " Bulk Heated Water" somewhere on the card

The logo with the flame large across the background might look ok? The name of the company is KESTREL BOILWORKS, but it probably isn't necessary to have the hot water under the logo all the time if you decide it looks better. As long as it is included somewhere on the card. The style of the Kestrel can change slightly (ie:; can be slanted).

The colors of the logo can change, but it might be nice to have the original color and logo somewhere small (corner?)

```html
<!DOCTYPE html>
<html lang="en">
<head>
<meta charset="utf-8">
<title>Kestrel Boilworks Business Card</title>
<link rel="stylesheet" href="https://fonts.googleapis.com/css2?family=Source+Sans+3:wght@400;600;700&display=swap">
<style>
  :root {
    --stage: #808080;
    --card-dark: #1c1c1c;
    --card-red: #ff0000;
    --accent-red: #ff2a00;
    --ink: #1a1a1a;
    --drop-blue: #1a86c0;
    --footer-shadow: rgba(60, 0, 0, 0.85);
  }
  * { margin: 0; padding: 0; box-sizing: border-box; }
  html, body {
    width: 1050px;
    height: 1200px;
    overflow: hidden;
    background: var(--stage);
    font-family: "Source Sans 3", "Myriad Pro", Arial, sans-serif;
  }
  .canvas { position: relative; width: 1050px; height: 1200px; }

  .card { position: absolute; width: 852px; height: 491px; overflow: hidden; }
  .card--front { left: 98px; top: 95px; background: var(--card-dark); }
  .card--back { left: 96px; top: 630px; background: var(--card-red); }

  .edge-bar { position: absolute; width: 13px; height: 226px; }
  .card--front .edge-bar { top: 133px; background: var(--accent-red); }
  .card--back .edge-bar { top: 92px; background: var(--ink); }
  .edge-bar--left { left: 0; }
  .edge-bar--right { right: 0; }

  .brand { position: absolute; display: flex; flex-direction: column; align-items: center; }
  .brand__mark { border-radius: 50%; background: var(--drop-blue); }
  .brand__name {
    font-weight: 700;
    text-align: center;
    letter-spacing: -1px;
    line-height: 0.95;
  }
  .card--front .brand { left: 0; right: 0; top: 62px; }
  .card--front .brand__mark { width: 120px; height: 120px; margin-bottom: 34px; }
  .card--front .brand__name { color: var(--card-red); font-size: 76px; }

  .card--back .brand { left: 50px; width: 232px; top: 92px; }
  .card--back .brand__mark { width: 68px; height: 68px; margin-bottom: 22px; }
  .card--back .brand__name { color: var(--ink); font-size: 40px; }

  .contact { position: absolute; left: 427px; top: 88px; color: var(--ink); }
  .contact__name { font-size: 32px; font-weight: 700; letter-spacing: -1.2px; margin-bottom: 22px; }
  .contact__lines { font-size: 25px; line-height: 37px; letter-spacing: -0.9px; }
  .contact__lines + .contact__lines { margin-top: 34px; }

  .footer-shade {
    position: absolute; left: 0; right: 0; top: 365px; height: 53px;
    background: linear-gradient(to bottom, rgba(60,0,0,0) 0%, var(--footer-shadow) 100%);
  }
  .footer {
    position: absolute; left: 0; right: 0; bottom: 0; height: 74px;
    background: var(--card-red);
    display: flex; justify-content: space-between; align-items: center;
    padding: 0 18px 0 13px;
    color: var(--ink);
    font-size: 22px;
    letter-spacing: -0.9px;
    white-space: nowrap;
  }
</style>
</head>
<body>
<main class="canvas">
  <section class="card card--front" aria-label="Card front">
    <div class="edge-bar edge-bar--left"></div>
    <div class="edge-bar edge-bar--right"></div>
    <div class="brand">
      <div class="brand__mark"></div>
      <p class="brand__name">KESTREL<br>BOILWORKS</p>
    </div>
  </section>

  <section class="card card--back" aria-label="Card back">
    <div class="edge-bar edge-bar--left"></div>
    <div class="edge-bar edge-bar--right"></div>
    <div class="brand">
      <div class="brand__mark"></div>
      <p class="brand__name">KESTREL<br>BOILWORKS</p>
    </div>
    <div class="contact">
      <h1 class="contact__name">DEAN VARGA</h1>
      <p class="contact__lines">SITE 317, BOX 4, COMP 2, RR5<br>VELLMOOR RIDGE, KR, T9K 4P3</p>
      <p class="contact__lines">11-07-52-3 W4M<br>HWY 734 BETWEEN RR57 &amp; RR58</p>
    </div>
    <div class="footer-shade"></div>
    <footer class="footer">
      <span>EMAIL INFO@KESTRELBOILWORKS-MAIL.COM</span>
      <span>PHONE&nbsp; 780-555-3817</span>
      <span>FAX 780-555-2964</span>
    </footer>
  </section>
</main>
</body>
</html>
```